bottle label/ product label for smoothies (ultra fresh)

Please create a bottle label for our smoothies for retail distribution.
It's important that the following key features are clearly stated:

Ultra-fresh

Handmade

No preservatives

Not heat-treated

No added sugar

The base of the product label should be transparent, so that the color and content of the smoothie can be seen clearly.

We are a young, dynamic company. Our values are honesty, ultra-freshness, and authenticity — and we are the only ones producing this type of product in our country. We are positioned in the premium segment.

Design style: Modern, clean, and natural — but not playful or childish.

Example product: Kelu Kelu (Mango, Pineapple, Lemon, Passion Fruit, Orange)

Wenn du möchtest, kann ich auch gleich einen konkreten Vorschlag für das Etikettendesign auf Englisch oder einen Entwurfstext für das Label selbst erstellen. Sag einfach Bescheid!

Target Market(s)

trade - convenience

Industry/Entity Type

trade

Font styles to use
Sans Serif

Requirements
Must have
• sales- features: Ultra-fresh Handmade No preservatives Not heat-treated No added sugar

```html
<!DOCTYPE html>
<html lang="en">
<head>
<meta charset="utf-8">
<title>VERANTA – Kelu Kelu Mango smoothie label</title>
<link href="https://fonts.googleapis.com/css2?family=Poppins:wght@400;500&family=Dancing+Script:wght@700&display=swap" rel="stylesheet">
<style>
  :root {
    --backdrop: #ececec;
    --label-top: #f9c88f;
    --label-bottom: #f1b06c;
    --ink: #1d1d1d;
    --mango-light: #ffc93c;
    --mango-deep: #f29a1b;
  }
  * { box-sizing: border-box; margin: 0; padding: 0; }
  html, body {
    width: 1200px;
    height: 1200px;
    overflow: hidden;
    background: var(--backdrop);
  }
  .canvas {
    position: relative;
    width: 1200px;
    height: 1200px;
    display: flex;
    align-items: center;
    justify-content: center;
  }
  .label {
    position: relative;
    width: 710px;
    height: 1080px;
    background: linear-gradient(160deg, var(--label-top), var(--label-bottom));
    color: var(--ink);
    text-align: center;
  }
  .brand-name {
    position: absolute;
    top: 80px;
    left: 0;
    right: 0;
    font-family: "Poppins", sans-serif;
    font-weight: 500;
    font-size: 62px;
    letter-spacing: 14px;
    padding-left: 14px;
    line-height: 1;
    color: var(--ink);
  }
  .product-name {
    position: absolute;
    top: 280px;
    left: 0;
    right: 0;
    font-family: "Dancing Script", cursive;
    font-weight: 700;
    font-size: 96px;
    line-height: 118px;
  }
  .fruit-art {
    position: absolute;
    top: 545px;
    left: 50%;
    width: 180px;
    height: 180px;
    margin-left: -90px;
    border-radius: 50%;
    background: radial-gradient(circle at 40% 38%, var(--mango-light), var(--mango-deep));
  }
  .features {
    position: absolute;
    top: 765px;
    left: 20px;
    right: 20px;
    display: flex;
    justify-content: space-between;
    list-style: none;
  }
  .feature {
    width: 134px;
    display: flex;
    flex-direction: column;
    align-items: center;
  }
  .feature-icon {
    width: 100px;
    height: 100px;
  }
  .feature-text {
    margin-top: 12px;
    font-family: "Poppins", sans-serif;
    font-size: 20px;
    font-weight: 400;
    line-height: 1.15;
  }
  .tagline {
    position: absolute;
    top: 1010px;
    left: 0;
    right: 0;
    font-family: "Poppins", sans-serif;
    font-weight: 500;
    font-size: 23px;
    letter-spacing: 1.5px;
  }
</style>
</head>
<body>
<main class="canvas">
  <section class="label">
    <h1 class="brand-name">VERANTA</h1>
    <h2 class="product-name">Kelu Kelu<br>Mango</h2>
    <div class="fruit-art" role="img" aria-label="Illustration of a mango with a sliced piece"></div>

    <ul class="features">
      <li class="feature">
        <svg class="feature-icon" viewBox="0 0 100 100" fill="none" stroke="#1d1d1d" stroke-width="3" stroke-linecap="round" stroke-linejoin="round" aria-hidden="true">
          <circle cx="50" cy="50" r="46"/>
          <path d="M34 68 C30 44 46 30 68 30 C70 54 56 68 34 68 Z"/>
          <path d="M34 68 L58 42"/>
        </svg>
        <span class="feature-text">Ultra-fresh</span>
      </li>
      <li class="feature">
        <svg class="feature-icon" viewBox="0 0 100 100" fill="none" stroke="#1d1d1d" stroke-width="3" stroke-linecap="round" stroke-linejoin="round" aria-hidden="true">
          <circle cx="50" cy="50" r="46"/>
          <circle cx="50" cy="40" r="11"/>
          <path d="M22 52 L30 70 L44 76"/>
          <path d="M78 52 L70 70 L56 76"/>
        </svg>
        <span class="feature-text">Handmade</span>
      </li>
      <li class="feature">
        <svg class="feature-icon" viewBox="0 0 100 100" fill="none" stroke="#1d1d1d" stroke-width="3" stroke-linecap="round" stroke-linejoin="round" aria-hidden="true">
          <circle cx="50" cy="50" r="46"/>
          <path d="M45 60 V26 a5 5 0 0 1 10 0 V60"/>
          <circle cx="50" cy="68" r="9"/>
          <path d="M18 18 L82 82"/>
        </svg>
        <span class="feature-text">No preservatives</span>
      </li>
      <li class="feature">
        <svg class="feature-icon" viewBox="0 0 100 100" fill="none" stroke="#1d1d1d" stroke-width="3" stroke-linecap="round" stroke-linejoin="round" aria-hidden="true">
          <circle cx="50" cy="50" r="46"/>
          <path d="M42 24 V74 M34 66 L42 74 L50 66"/>
          <path d="M58 24 V74 M50 66 L58 74 L66 66"/>
          <path d="M18 18 L82 82"/>
        </svg>
        <span class="feature-text">Not heat-treated</span>
      </li>
      <li class="feature">
        <svg class="feature-icon" viewBox="0 0 100 100" fill="none" stroke="#1d1d1d" stroke-width="3" stroke-linecap="round" stroke-linejoin="round" aria-hidden="true">
          <circle cx="50" cy="50" r="46"/>
          <path d="M50 28 L70 38 V62 L50 72 L30 62 V38 Z"/>
          <path d="M30 38 L50 48 L70 38 M50 48 V72"/>
          <path d="M18 18 L82 82"/>
        </svg>
        <span class="feature-text">No added sugar</span>
      </li>
    </ul>

    <p class="tagline">PREMIUM | AUTHENTIC | PIONEERS</p>
  </section>
</main>
</body>
</html>
```